依頼詳細
商品は布マスクになりますが、取り急ぎ添付の不織布マスクの内容で構いせん。
全体のイメージで決定したいと思います。
決定後に布マスクの詳細をお伝えしますので、完成品に仕上げて頂きたいと思います。

製品形状はPP袋(PPのベースは透明もしくはアルミ銀)
袋サイズ:W130xH180mm+ヘッダー部分H20mm

印刷は4色分解でも構いませんが、中国印刷の為、あまり複雑過ぎない程度の色使いでお願いします。

急ぎ提案なのでイメージだけでも早く提案してもらえば助かります。
説明不足で申し訳ございませんが、不明点はご連絡お願い致します。
記載項目
PP袋(PPのベースは透明もしくはアルミ銀)

印刷は4色分解でも構いませんが、中国グラビア印刷(8色まで)の為、あまり複雑過ぎない程度の色使いでお願いします。版代のコストも抑えたいです。
希望イメージ
シンプル 複雑
単色 カラフル
暗い 明るい
日常 高級
遊び心 厳粛
未来的 伝統的
女性的 男性的
希望する色
青系、水色系、無彩色系
納品ファイル
• イラストレーター形式 (.ai)
補足説明

お客様の選定により

たくさんのご提案ありがとうございました
またの機会にも是非またご提案お願い致します。

```html
<!DOCTYPE html>
<html lang="ja">
<head>
<meta charset="utf-8">
<title>布マスク パッケージ</title>
<link rel="stylesheet" href="https://fonts.googleapis.com/css2?family=Noto+Sans+JP:wght@400;500;700;900&display=swap">
<style>
  :root {
    --ink: #3a3a3a;
    --blue: #1a86d0;
    --blue-deep: #0f6fb8;
    --blue-light: #d8ecf8;
    --red: #e60012;
    --line: #bdbdbd;
    --paper: #ffffff;
    --bg: #f1f1f1;
  }
  * { box-sizing: border-box; margin: 0; padding: 0; }
  html, body { width: 884px; height: 1200px; overflow: hidden; background: var(--bg); }
  body { font-family: "Noto Sans JP", sans-serif; color: var(--ink); }
  .package {
    position: absolute; left: 14px; top: 10px; width: 856px; height: 1180px;
    background: var(--paper); border: 2px solid #d6d6d6; overflow: hidden;
  }
  .size-tag {
    position: absolute; left: 74px; top: 80px; width: 134px; height: 48px;
    background: var(--blue); color: #fff; border-radius: 10px;
    font-weight: 700; font-size: 26px; line-height: 48px; text-align: center;
  }
  .size-tag small { font-size: 18px; }
  .size-dim { position: absolute; left: 224px; top: 82px; font-size: 20px; line-height: 1.15; }
  .hang-hole {
    position: absolute; left: 432px; top: 98px; width: 24px; height: 24px;
    border-radius: 50%; border: 2px solid var(--line); background: #fff;
  }
  .claim { position: absolute; left: 156px; top: 196px; font-weight: 700; font-size: 46px; line-height: 1.25; letter-spacing: 1px; }
  .claim-number { position: absolute; left: 540px; top: 172px; font-weight: 900; font-size: 118px; line-height: 1; color: var(--ink); }
  .claim-number span { font-size: 80px; }
  .claim-rule { position: absolute; left: 110px; top: 316px; width: 660px; height: 3px; background: var(--ink); }
  .product-seal {
    position: absolute; left: 218px; top: 344px; width: 440px; height: 440px;
    border-radius: 50%; background: #fff; border: 3px solid #e2e2e2;
    box-shadow: 0 4px 18px rgba(0,0,0,.12); text-align: center;
  }
  .seal-title { margin-top: 72px; font-weight: 900; font-size: 92px; line-height: 1.1; letter-spacing: 4px; }
  .seal-rule { width: 320px; height: 3px; background: var(--ink); margin: 18px auto 20px; }
  .seal-material { font-weight: 700; font-size: 50px; line-height: 1.1; }
  .seal-origin { margin-top: 26px; font-weight: 900; font-size: 62px; color: var(--red); letter-spacing: 4px; }
  .blue-band { position: absolute; left: 0; top: 0; width: 856px; height: 1180px; }
  .mask-art { position: absolute; left: 40px; top: 880px; width: 340px; height: 230px; border-radius: 30px; }
  .count { position: absolute; left: 630px; top: 810px; font-weight: 700; font-size: 54px; }
  .count span { font-size: 42px; }
  .filters { position: absolute; left: 450px; top: 936px; display: grid; grid-template-columns: 150px 150px; gap: 20px 50px; }
  .filter-chip {
    height: 42px; border: 2px solid var(--ink); font-size: 22px; font-weight: 500;
    text-align: center; line-height: 38px; white-space: nowrap; letter-spacing: -0.5px;
  }
</style>
</head>
<body>
<div class="package">
  <svg class="blue-band" viewBox="0 0 856 1180" aria-hidden="true">
    <path d="M0 770 C150 790 300 850 430 960 C500 1030 560 1110 600 1180 L0 1180 Z" fill="var(--blue-deep)"/>
    <path d="M0 800 C150 820 290 880 410 980 C470 1040 520 1110 555 1180 L0 1180 Z" fill="var(--blue)"/>
  </svg>
  <div class="mask-art" role="img" aria-label="耳ひも付きプリーツマスクのイラスト" style="background:linear-gradient(160deg,#ffffff,#e6eef5);"></div>

  <div class="size-tag">ふつう<small>サイズ</small></div>
  <div class="size-dim">95×<br>35mm</div>
  <div class="hang-hole"></div>

  <div class="claim">ウイルス飛沫<br>カットフィルター</div>
  <div class="claim-number">99<span>%</span></div>
  <div class="claim-rule"></div>

  <div class="product-seal">
    <div class="seal-title">布マスク</div>
    <div class="seal-rule"></div>
    <div class="seal-material">コットン100%</div>
    <div class="seal-origin">日本製</div>
  </div>

  <div class="count">3<span>枚入</span></div>
  <div class="filters">
    <div class="filter-chip">花粉</div>
    <div class="filter-chip">ハウスダスト</div>
    <div class="filter-chip">ウイルス粉末</div>
    <div class="filter-chip">PM2.5</div>
  </div>
</div>
</body>
</html>
```